Web Design Nutrition supplements (Quillstack 5 pages)

We are looking for templates for a new nutrition supplement shop www.velmorida.ch , targeting Swiss Female 65% /Male 35% over 40 yrs with high quality products (no performance enhancement /Body building products).
Our customers are not the most proficient in internet, so the website should be simple, easily understood. not too much web2.0 look and feel and functionality.

velmorida.ch product offerings are high quality and supplied from top brands: like Dr. Wentholm, Soravin, talbrücken, Nalvimed), for diets, weight management, antistress, anti-apathy, oligo-elements, omega-3 oils, and cosmetics.

We want the website design
1) to reflect our seriousness and expertise in the area,
2)to Inspire trust from our customers and address their needs in a personal and professional way (we answer your questions over email/Phone)
3) though we are not an pharmacy, our products are currently sold in pharmacies in Switzerland, so we want our customers to feel as well served online, as if they were in a pharmacy.
4) compare favorably to international websites (F, G) also selling online to Swiss customers: we are a truly Swiss company and can deliver within less than 18 h. in Switzerland (so the Swiss flag is an important design element for us)

We want to provide a superior buying experience,
1) important: providing sufficient product information: (intelligible snippet/summary of product info) should be visible on search result pages, and category pages,
2) clarity of design "emphasis" on products with clear call to action (buy)

Deliverables for the winning designer;
Photoshop files that can be easily be integrated in our quillstack shop.
- Homepage
- Category Page
- Product Page
For 1st evaluation and corrections of the proposals.

- Landing Page (for SEM Campaigns)
- Newsletter (Post raven)
as a second step.

Please use the attached wireframes, that should give you the exact content we want to provide (as well as functionality), the wireframes donnot define the user experience/design (it s more like a guidance, suggestion)

Target Market(s)

Swiss Males /35% Females 65% (both Swiss French/ Swiss German over 40 years

Industry/Entity Type

Nutrition

Requirements
Must have
• Deliverables:
- Homepage
- Category Page
- Product Page

- Newsletter template
- Landing Page

We attach:
- navigation to show how users can access the products (cat/ sub cat, but also search for body parts, objectives of healing... (see Kategorien-for-web.xls)
- Wireframes (myKrondelo)
- Logo (1 psd)
- Product images (zip files)
- Benchmarks: vitorelle.co.uk (simplicity), pmv.com (expandable navigation),
- Competitors: ko7.de, tramelo.com, tramelo-deutschland.de, quint-fold.eu

```html
<!DOCTYPE html>
<html lang="en">
<head>
<meta charset="utf-8">
<title>velmorida – Nutrition supplements</title>
<link href="https://fonts.googleapis.com/css2?family=Ubuntu:wght@400;500;700&family=PT+Sans:wght@400;700&display=swap" rel="stylesheet">
<style>
:root{
  --green:#79aa10;
  --green-dark:#5a8a08;
  --green-deep:#1f6e1c;
  --teal:#4e7d8c;
  --grey-text:#4f4f4f;
  --light-text:#6b6b6b;
  --panel:#f2f2f2;
  --border:#cfcfcf;
  --white:#fff;
}
*{box-sizing:border-box;margin:0;padding:0}
html,body{width:1200px;height:1196px;overflow:hidden}
body{position:relative;background:#fff;font-family:"PT Sans",sans-serif;color:var(--grey-text)}
.abs{position:absolute}
/* header */
.brand{left:128px;top:50px;display:flex;align-items:center;gap:10px}
.brand-mark{width:56px;height:56px;border:5px solid var(--teal);border-radius:8px}
.brand-name{font-family:"Ubuntu",sans-serif;font-size:44px;color:var(--teal);font-weight:400;letter-spacing:1px}
.usp{display:flex;align-items:center;gap:8px;top:70px}
.usp-title{font-family:"Ubuntu",sans-serif;font-weight:700;font-size:17px;color:var(--green);line-height:1}
.usp-small{font-size:9px;line-height:1;color:#333;text-transform:uppercase}
.usp-sep{top:72px;width:1px;height:52px;background:#ddd}
.search{left:918px;top:73px;width:236px;height:31px;border:2px solid #e4e4e4;border-radius:16px;font-size:11px;padding:7px 14px;color:#333}
.account{left:962px;top:118px;font-size:12px;color:#333;display:flex;gap:4px;align-items:center}
.lang{left:935px;top:172px;font-size:11px;color:#333;display:flex;gap:6px;align-items:center}
.flag{display:inline-block;width:16px;height:11px}
/* nav */
.nav{left:0;top:192px;width:1200px;height:40px;background:var(--green)}
.nav ul{list-style:none;display:flex;position:absolute;left:110px;top:0;height:40px}
.nav li{font-size:14px;color:#fff;line-height:40px;padding:0 11px}
.nav li.active{background:var(--green-dark);color:#b9dd5a;padding:0 8px;margin-right:9px}
/* content */
.stage{left:0;top:232px;width:1200px;height:190px;background:linear-gradient(#eaeaea,#f5f5f5)}
.panel{left:104px;top:232px;width:998px;height:666px;background:var(--panel);box-shadow:0 0 14px rgba(0,0,0,.12)}
.sidebar{left:122px;top:250px;width:172px;height:219px;background:#f6f6f6;border:1px solid var(--border)}
.side-head{background:var(--green);color:#fff;font-family:"Ubuntu",sans-serif;font-weight:500;font-size:13px;height:27px;line-height:27px;padding-left:16px}
.side-list{list-style:none;font-size:10px;color:#333;padding-left:16px}
.side-list li{height:20px;line-height:20px}
.slider{left:311px;top:251px;width:542px;height:218px;background:#fff;border:1px solid var(--border);overflow:hidden}
.slide-tag{position:absolute;left:0;top:74px;width:159px;height:46px;background:var(--green);color:#fff;font-family:"Ubuntu",sans-serif;font-size:24px;line-height:46px;padding-left:5px}
.photo{position:absolute}
.slide-pct{position:absolute;left:342px;top:6px;font-family:"Ubuntu",sans-serif;font-weight:700;font-size:82px;color:var(--green);line-height:1}
.slide-title{position:absolute;left:342px;top:84px;font-family:"Ubuntu",sans-serif;font-size:28px;color:var(--grey-text)}
.slide-copy{position:absolute;left:342px;top:116px;width:185px;font-size:9.5px;line-height:13px;text-align:justify;color:#555}
.arrow{position:absolute;top:172px}
.care{left:884px;top:251px;width:203px;height:221px;background:var(--green)}
.care-label{position:absolute;left:16px;top:112px;font-family:"Ubuntu",sans-serif;font-weight:500;font-size:34px;line-height:32px;color:#fff}
.care-phone{position:absolute;left:16px;top:177px;font-family:"Ubuntu",sans-serif;font-weight:500;font-size:22px;color:#fff}
.care-hours{position:absolute;left:3px;top:10px;font-family:"Ubuntu",sans-serif;font-weight:700;font-size:12px;color:#444}
.card{top:502px;width:294px;height:168px;background:#fff;border:1px solid var(--border)}
.card h3{position:absolute;left:24px;top:20px;font-family:"Ubuntu",sans-serif;font-weight:400;font-size:34px;line-height:32px;color:var(--grey-text)}
.card p{position:absolute;left:25px;top:96px;width:160px;font-size:11px;line-height:16px;text-align:justify;color:#777}
.offer{top:707px;width:213px;height:171px;background:#fff;border:1px solid var(--border)}
.offer svg.flagtag{position:absolute;left:14px;top:-12px}
.offer .tagtext{position:absolute;left:22px;top:0;font-family:"Ubuntu",sans-serif;font-weight:500;font-size:21px;line-height:23px;color:#fff}
/* footer */
.footer{left:0;top:898px;width:1200px;height:298px;background:var(--green);color:#fff}
.fcol{position:absolute;top:58px}
.fcol h4{font-family:"PT Sans",sans-serif;font-weight:400;font-size:20px;margin-bottom:20px;letter-spacing:-.3px}
.fcol ul{list-style:none;font-size:13px;line-height:18px}
.social{position:absolute;left:158px;top:194px;display:flex;gap:8px}
.social span{width:32px;height:32px;border-radius:4px;background:#fff;opacity:.85}
.tiles{position:absolute;left:804px;top:59px;display:grid;grid-template-columns:repeat(3,77px);gap:15px 20px}
.tile{height:67px;background:#eef1ea;display:flex;align-items:center;justify-content:center}
.tile i{width:30px;height:30px;border:5px solid var(--teal);border-radius:5px;display:block}
.fbottom{position:absolute;top:256px;left:161px;display:flex;gap:33px;font-size:11px}
.copy{position:absolute;left:790px;top:255px;font-size:11px}
</style>
</head>
<body>

<header>
  <div class="abs brand"><span class="brand-mark"></span><span class="brand-name">velmorida</span></div>

  <div class="abs usp" style="left:454px">
    <svg width="42" height="42" viewBox="0 0 42 42"><circle cx="21" cy="21" r="18" fill="none" stroke="#444" stroke-width="3"/><path d="M21 9v12l7 5" stroke="#444" stroke-width="2.5" fill="none"/></svg>
    <div><div class="usp-title">DELIVERY</div><div class="usp-small">in Switzerland<br>is less than</div><div class="usp-title" style="font-size:14px">18 HOURS</div></div>
  </div>
  <div class="abs usp-sep" style="left:610px"></div>
  <div class="abs usp" style="left:626px">
    <svg width="32" height="44" viewBox="0 0 32 44"><path d="M16 43 4 26A15 15 0 1 1 28 26Z" fill="#444"/><circle cx="16" cy="15" r="11" fill="#fff"/><text x="16" y="19" text-anchor="middle" font-size="11" font-weight="700" font-family="Ubuntu,sans-serif" fill="#333">80</text></svg>
    <div><div class="usp-title" style="font-size:19px">FREE</div><div class="usp-small" style="font-size:10px">delivery<br>from 80</div><div class="usp-small" style="font-size:6px">Swiss franc</div></div>
  </div>
  <div class="abs usp-sep" style="left:740px"></div>
  <div class="abs usp" style="left:760px">
    <svg width="40" height="50" viewBox="0 0 40 50"><rect x="18" y="2" width="4" height="46" fill="#444"/><path d="M0 12q10-4 18 2M40 12q-10-4-18 2" stroke="#444" stroke-width="4" fill="none"/><path d="M14 20q12 4 0 9q12 4 0 9" stroke="#444" stroke-width="2" fill="none"/></svg>
    <div><div class="usp-title" style="font-size:19px">EXPERTS</div><div style="font-size:11px;color:#333">HELP YOU</div></div>
  </div>

  <div class="abs search">Search your Item (eg.
    <svg style="position:absolute;right:10px;top:6px" width="20" height="16" viewBox="0 0 20 16"><circle cx="7" cy="7" r="5.5" fill="none" stroke="#bbb" stroke-width="2"/><path d="M11 10l7 5" stroke="#bbb" stroke-width="3"/></svg>
  </div>
  <div class="abs account">My account | Shopping cart
    <svg width="20" height="16" viewBox="0 0 20 16"><path d="M0 2h4l3 9h10l2-7H6" fill="none" stroke="#444" stroke-width="2"/><circle cx="8" cy="14" r="1.6" fill="#444"/><circle cx="16" cy="14" r="1.6" fill="#444"/></svg>
  </div>
  <div class="abs lang">Help | Select the language
    <span class="flag" style="background:linear-gradient(#000 33%,#d00 33% 66%,#fc0 66%)"></span>DE
    <span class="flag" style="margin-left:12px;background:linear-gradient(90deg,#0a3ea4 33%,#fff 33% 66%,#e1001a 66%)"></span>FR
  </div>
</header>

<nav class="abs nav">
  <ul>
    <li class="active">Vitamins &amp; Minerals</li>
    <li>Essential Feautres</li>
    <li style="padding:0 14px">Proteins</li>
    <li>Spirulina maca</li>
    <li>Gewichtasabnahme</li>
    <li>Cosmetics</li>
    <li style="padding-right:30px">Physiotheraphy</li>
    <li>Functions</li>
    <li style="padding-left:8px">Antibiotics</li>
  </ul>
</nav>

<main>
  <div class="abs stage"></div>
  <div class="abs panel"></div>

  <aside class="abs sidebar">
    <div class="side-head">HEALTH</div>
    <ul class="side-list" style="padding-top:17px;padding-bottom:3px">
      <li>Allergy &amp; Intolerance</li><li>An unbalanced diet</li><li>Energy budget</li><li>Detoxify, Purify</li>
    </ul>
    <div class="side-head">BODY</div>
    <ul class="side-list" style="padding-top:0">
      <li>Eye</li><li>Legs and veins</li><li>Joints and bones</li>
    </ul>
  </aside>

  <section class="abs slider">
    <div class="slide-tag">Lorem Ipsum</div>
    <div class="photo" role="img" aria-label="Supplement box product photo" style="left:178px;top:16px;width:115px;height:152px;background:linear-gradient(135deg,#ffffff,#f0ece6 60%,#e9a77f)"></div>
    <div class="slide-pct">25%</div>
    <div class="slide-title">Lorem Ipsum</div>
    <p class="slide-copy">is simply dummy text of the printing and typesetting industry. Lorem Ipsum has been the industry's standard dummy text ever since the 1500s,</p>
    <svg class="arrow" style="left:16px" width="26" height="30" viewBox="0 0 26 30"><path d="M20 3 7 15l13 12" fill="none" stroke="#555" stroke-width="6"/></svg>
    <svg class="arrow" style="left:492px" width="26" height="30" viewBox="0 0 26 30"><path d="M6 3l13 12L6 27" fill="none" stroke="#555" stroke-width="6"/></svg>
  </section>

  <section class="abs care">
    <div class="photo" role="img" aria-label="Photo of a smiling support agent with headset" style="left:0;top:0;width:203px;height:111px;background:linear-gradient(90deg,#f4f4f4 30%,#e8d2c2 60%,#f1f1f1)"></div>
    <div class="care-hours">24x7</div>
    <div class="care-label">Customer<br>Care</div>
    <div class="care-phone">030-512868 40</div>
  </section>

  <article class="abs card" style="left:140px">
    <h3>Lorem<br>Ipsum</h3>
    <p>typesetting industry. Lorem Ipsum has been the industry's standard dummy text ever since the 1500s,</p>
    <div class="photo" role="img" aria-label="Supplement bottle product photo" style="left:204px;top:16px;width:66px;height:124px;border-radius:10px;background:linear-gradient(#1f2a55 30%,#e9e4e6 30% 75%,#8c1f3a 75%)"></div>
  </article>
  <article class="abs card" style="left:456px">
    <h3>Lorem<br>Ipsum</h3>
    <p>typesetting industry. Lorem Ipsum has been the industry's standard dummy text ever since the 1500s,</p>
    <div class="photo" role="img" aria-label="Supplement bottle product photo" style="left:194px;top:16px;width:62px;height:124px;border-radius:10px;background:linear-gradient(#eeeeee 25%,#d4242e 25% 60%,#f2f2f2 60%)"></div>
  </article>
  <article class="abs card" style="left:771px">
    <h3 style="top:30px">Lorem<br>Ipsum</h3>
    <p>typesetting industry. Lorem Ipsum has been the industry's standard dummy text ever since the 1500s,</p>
    <div class="photo" role="img" aria-label="Supplement bottle product photo" style="left:190px;top:16px;width:66px;height:124px;border-radius:10px;background:linear-gradient(#1d3fa0 30%,#f1eef2 30% 78%,#1e5cc0 78%)"></div>
  </article>

  <article class="abs offer" style="left:140px">
    <div class="photo" role="img" aria-label="Supplement box product photo" style="left:72px;top:26px;width:92px;height:120px;background:linear-gradient(135deg,#fff,#f0ece6 60%,#e99a6a)"></div>
    <svg class="flagtag" width="94" height="96" viewBox="0 0 94 96"><path d="M6 0h88l-14 48q-12 44-74 48Z" fill="var(--green-deep)"/></svg>
    <div class="tagtext">Special<br>&nbsp;Offer<br>25%</div>
  </article>
  <article class="abs offer" style="left:376px">
    <div class="photo" role="img" aria-label="Supplement jar product photo" style="left:80px;top:30px;width:62px;height:118px;border-radius:8px;background:linear-gradient(#d7e6f0 25%,#f4f4f4 25%)"></div>
    <svg class="flagtag" width="94" height="96" viewBox="0 0 94 96"><path d="M6 0h88l-14 48q-12 44-74 48Z" fill="var(--green-deep)"/></svg>
    <div class="tagtext">Special<br>&nbsp;Offer<br>25%</div>
  </article>
  <article class="abs offer" style="left:613px">
    <div class="photo" role="img" aria-label="Supplement box product photo" style="left:86px;top:24px;width:76px;height:124px;background:linear-gradient(135deg,#fff,#eef4f8 60%,#6cb4e0)"></div>
    <svg class="flagtag" width="94" height="96" viewBox="0 0 94 96"><path d="M6 0h88l-14 48q-12 44-74 48Z" fill="var(--green-deep)"/></svg>
    <div class="tagtext">Special<br>&nbsp;Offer<br>25%</div>
  </article>
  <article class="abs offer" style="left:851px">
    <div class="photo" role="img" aria-label="Supplement box product photo" style="left:86px;top:24px;width:76px;height:124px;background:linear-gradient(135deg,#fff,#eef4f8 60%,#6cb4e0)"></div>
    <svg class="flagtag" width="94" height="96" viewBox="0 0 94 96"><path d="M6 0h88l-14 48q-12 44-74 48Z" fill="var(--green-deep)"/></svg>
    <div class="tagtext">Special<br>&nbsp;Offer<br>25%</div>
  </article>
</main>

<footer class="abs footer">
  <div class="fcol" style="left:162px;top:60px">
    <h4>ABOUT</h4>
    <ul><li>News &amp; Reviews</li><li>Events</li><li>Technology</li><li>Teams &amp; Conditions</li></ul>
  </div>
  <div class="fcol" style="left:318px;top:57px">
    <h4>SUPPORT</h4>
    <ul><li>&nbsp;Archive</li><li>Register your bike</li><li>Privacy Policy / Disclaimer</li></ul>
  </div>
  <div class="fcol" style="left:504px;top:60px">
    <h4>COMPANY</h4>
    <ul><li>About</li><li>Join ou company</li><li>&nbsp;Websites</li></ul>
  </div>
  <div class="social" aria-label="Social links"><span></span><span></span><span></span><span></span></div>
  <div class="tiles">
    <div class="tile"><i></i></div><div class="tile"><i></i></div><div class="tile"><i></i></div>
    <div class="tile"><i></i></div><div class="tile"><i></i></div><div class="tile"><i></i></div>
  </div>
  <div class="fbottom"><span>HOME</span><span>SERVICES</span><span>ABOUT US</span><span>CAREERS</span><span>TERMS &amp; CONDITIONS</span><span>CONTACT US</span></div>
  <div class="copy">Copyright © 2012 www.velmorida.com. All Rights Reserved.</div>
</footer>

</body>
</html>
```